Elegant Business Cards & Letterhead

We will need the following that need to be designed: Letterhead and Business Cards, there winer will be re-hired for the balance of our stationary needs. Text for the cards and letterheads:

- Corporate Card instead of name
- landline: +971 (4) 362 7041
- mobile: +971 56 2819 605
- 800TUTOR
- email: dubai@velmora-lune.com
- www.velmora-lune.com
- PO Box 387261
Address: Castellan Heights Suite 1708, Dubai UAE

Thank you

Target Market(s)

VIPs, HNWI, High-end Families.

Industry/Entity Type

Luxury Market

Font styles to use
Other font styles liked:
• as explained

Colors

Designer to choose only greyscale colors for use in the design.

Requirements
Must have
• Elegant, Simple, Luxurious, Minimalistic
Nice to have
• Luxury, Golds, Engravings,
Should not have
• Much colors, funky,

```html
<!DOCTYPE html>
<html lang="en">
<head>
<meta charset="utf-8">
<title>Velmora Lune — Business Cards</title>
<link href="https://fonts.googleapis.com/css2?family=Marcellus&family=Arimo:wght@400&display=swap" rel="stylesheet">
<style>
  :root {
    --canvas: #e4e4e4;
    --card-light: #fbfbfb;
    --card-dark: #050505;
    --ink-dark: #111111;
    --ink-light: #f2f2f2;
    --ink-muted: #e6e6e6;
    --rule-light: #d8d8d8;
  }
  * { margin: 0; padding: 0; box-sizing: border-box; }
  html, body {
    width: 1200px; height: 779px; overflow: hidden;
    background: var(--canvas);
  }
  .stage { position: relative; width: 1200px; height: 779px; }

  .card {
    position: absolute;
    width: 525px; height: 300px;
    border-radius: 22px;
    box-shadow: 0 10px 28px rgba(0,0,0,0.18);
  }
  .card--front {
    left: 80px; top: 70px;
    background: var(--card-light);
    color: var(--ink-dark);
  }
  .card--back {
    left: 595px; top: 409px;
    background: var(--card-dark);
    color: var(--ink-light);
  }

  .wordmark {
    font-family: "Marcellus", "Optima", serif;
    letter-spacing: 0.04em;
    white-space: nowrap;
  }
  .card--front .wordmark {
    position: absolute; left: 0; right: 0; top: 108px;
    text-align: center; font-size: 44px;
  }
  .card--front .web {
    position: absolute; left: 0; right: 0; bottom: 46px;
    text-align: center;
    font-family: "Arimo", Arial, sans-serif;
    font-size: 12px; letter-spacing: 0.28em;
  }

  .card--back .wordmark {
    position: absolute; left: 36px; top: 132px;
    font-size: 27px; color: var(--ink-light);
  }
  .card--back .divider {
    position: absolute; left: 298px; top: 42px;
    width: 1px; height: 168px; background: var(--rule-light);
  }
  .contact {
    position: absolute; left: 316px; top: 40px;
    font-family: "Arimo", Arial, sans-serif;
    font-size: 12.5px; line-height: 15px;
    color: var(--ink-muted);
  }
  .contact address { font-style: normal; margin-bottom: 10px; }
  .contact ul { list-style: none; }
  .contact li { display: flex; align-items: center; gap: 7px; }
  .contact svg { width: 10px; height: 10px; fill: var(--ink-muted); flex: none; }
</style>
</head>
<body>
<main class="stage">
  <section class="card card--front" aria-label="Card front">
    <h1 class="wordmark">VELMORA LUNE</h1>
    <p class="web">www.velmora-lune.com</p>
  </section>

  <section class="card card--back" aria-label="Card back">
    <h2 class="wordmark">VELMORA LUNE</h2>
    <div class="divider"></div>
    <div class="contact">
      <address>
        PO Box 387261<br>
        Castellan Heights<br>
        Suite 1708, Dubai UAE
      </address>
      <ul>
        <li><svg viewBox="0 0 10 10" aria-hidden="true"><path d="M2 0.5 L3.6 2.6 L2.6 3.6 Q3.6 5.8 6.4 7.4 L7.4 6.4 L9.5 8 L8.2 9.5 Q4.5 9.2 1.5 5.5 Q0.3 3.6 0.5 1.8 Z"/></svg>+971 (4) 362 7041</li>
        <li><svg viewBox="0 0 10 10" aria-hidden="true"><path d="M2 0.5 L3.6 2.6 L2.6 3.6 Q3.6 5.8 6.4 7.4 L7.4 6.4 L9.5 8 L8.2 9.5 Q4.5 9.2 1.5 5.5 Q0.3 3.6 0.5 1.8 Z"/></svg>800TUTOR</li>
        <li><svg viewBox="0 0 10 10" aria-hidden="true"><path d="M2.5 0 H7.5 V10 H2.5 Z M3.4 1 V8 H6.6 V1 Z"/></svg>+971 56 2819 605</li>
        <li><svg viewBox="0 0 10 10" aria-hidden="true"><path d="M0 2 H10 V8.5 H0 Z M0.8 2.6 L5 5.6 L9.2 2.6 V3.4 L5 6.4 L0.8 3.4 Z" fill-rule="evenodd"/></svg>dubai@velmora-lune.com</li>
        <li><svg viewBox="0 0 10 10" aria-hidden="true"><circle cx="5" cy="5" r="4.8"/></svg>www.velmora-lune.com</li>
      </ul>
    </div>
  </section>
</main>
</body>
</html>
```